New Label Design Project

I need a coffee label that i can edit based on the designs we first came up with. The coffee bags i will use are 250g side gusseted Matt black so it can capture the colours in the logos.. My issue is that i need to add information regarding the type of coffee I am selling - Im using 5 single origin sourced coffee and the beans are all 100% arabica and ill add some information on the current stock I’m using… Im out of ideas at the moment! but want to keep it clean and fresh… Information I must have is weight… 250g and roasted on date (best used within 3 months of date). anything else will be considered?! Ill attached the logos / references and also the website which is still under development… www.tqcoffee.co.uk

```html
<!DOCTYPE html>
<html lang="en">
<head>
<meta charset="utf-8">
<title>Tidequay Roastery Coffee – 250g Bag Label</title>
<link rel="stylesheet" href="https://fonts.googleapis.com/css2?family=Oswald:wght@400;500;600&family=Roboto:wght@300;400&display=swap">
<style>
  :root {
    --bag-black: #000000;
    --label-line: #d9d4cc;
    --copper: #c47f2c;
    --cream: #efe4cc;
    --dot: #c47f2c;
    --roast-dark: #1c0f08;
    --roast-mid: #3e1f10;
    --roast-warm: #5a3019;
  }
  * { margin: 0; padding: 0; box-sizing: border-box; }
  html, body {
    width: 1200px;
    height: 4193px;
    overflow: hidden;
    background: var(--bag-black);
  }
  .bag {
    position: relative;
    width: 1200px;
    height: 4193px;
    background: var(--bag-black);
  }
  .label {
    position: absolute;
    left: 112px;
    top: 1415px;
    width: 973px;
    height: 2252px;
    border: 3px solid var(--label-line);
    background: var(--bag-black);
  }
  .brand {
    position: absolute;
    left: 0;
    width: 100%;
    top: 240px;
    height: 450px;
    display: flex;
    flex-direction: column;
    align-items: center;
    justify-content: center;
    gap: 40px;
  }
  .brand-dot {
    width: 110px;
    height: 110px;
    border-radius: 50%;
    background: var(--copper);
  }
  .brand-name {
    font-family: "Oswald", sans-serif;
    font-weight: 600;
    font-size: 78px;
    line-height: 1.15;
    letter-spacing: 6px;
    color: var(--copper);
    text-align: center;
    text-transform: uppercase;
  }
  .bean-claim {
    position: absolute;
    left: 0;
    width: 100%;
    top: 925px;
    text-align: center;
    font-family: "Oswald", sans-serif;
    color: var(--cream);
  }
  .bean-claim .percent {
    display: block;
    font-weight: 600;
    font-size: 128px;
    line-height: 1;
    transform: scaleX(0.82);
  }
  .bean-claim .variety {
    display: block;
    font-weight: 500;
    font-size: 42px;
    line-height: 1;
    margin-top: 2px;
    transform: scaleX(0.82);
  }
  .notes {
    position: absolute;
    left: 134px;
    width: 694px;
    top: 1212px;
  }
  .dotted-rule {
    display: block;
    width: 100%;
    height: 8px;
  }
  .note-line {
    font-family: "Roboto", sans-serif;
    font-weight: 300;
    font-size: 40px;
    letter-spacing: 4px;
    color: var(--cream);
    text-align: center;
    line-height: 1;
    padding: 26px 0 28px;
  }
  .beans-photo {
    position: absolute;
    left: 0;
    top: 1507px;
    width: 100%;
    height: 540px;
    background: linear-gradient(165deg, var(--bag-black) 0%, var(--roast-dark) 35%, var(--roast-mid) 70%, var(--roast-warm) 100%);
  }
  .weight {
    position: absolute;
    left: 0;
    width: 100%;
    top: 2045px;
    text-align: center;
    font-family: "Oswald", sans-serif;
    font-weight: 500;
    font-size: 70px;
    line-height: 1;
    color: var(--copper);
  }
  .roast-date {
    position: absolute;
    left: 0;
    width: 100%;
    top: 2132px;
    text-align: center;
    font-family: "Roboto", sans-serif;
    font-weight: 400;
    font-size: 26px;
    letter-spacing: 7px;
    line-height: 1;
    color: var(--cream);
  }
  .best-before {
    position: absolute;
    left: 0;
    width: 100%;
    top: 2182px;
    text-align: center;
    font-family: "Roboto", sans-serif;
    font-weight: 400;
    font-size: 30px;
    letter-spacing: 9px;
    line-height: 1;
    color: var(--cream);
  }
</style>
</head>
<body>
  <main class="bag">
    <section class="label">
      <div class="brand">
        <span class="brand-dot"></span>
        <p class="brand-name">Tidequay<br>Roastery Coffee</p>
      </div>

      <p class="bean-claim">
        <span class="percent">100%</span>
        <span class="variety">ARABICA</span>
      </p>

      <div class="notes">
        <svg class="dotted-rule" viewBox="0 0 694 8" preserveAspectRatio="none" aria-hidden="true">
          <line x1="4" y1="4" x2="690" y2="4" stroke="var(--dot)" stroke-width="6" stroke-linecap="round" stroke-dasharray="0 32.6"/>
        </svg>
        <p class="note-line">This only for reference</p>
        <svg class="dotted-rule" viewBox="0 0 694 8" preserveAspectRatio="none" aria-hidden="true">
          <line x1="4" y1="4" x2="690" y2="4" stroke="var(--dot)" stroke-width="6" stroke-linecap="round" stroke-dasharray="0 32.6"/>
        </svg>
        <p class="note-line">Write what you want to</p>
        <svg class="dotted-rule" viewBox="0 0 694 8" preserveAspectRatio="none" aria-hidden="true">
          <line x1="4" y1="4" x2="690" y2="4" stroke="var(--dot)" stroke-width="6" stroke-linecap="round" stroke-dasharray="0 32.6"/>
        </svg>
      </div>

      <div class="beans-photo" role="img" aria-label="Photograph of a hessian sack spilling roasted coffee beans onto a dark wooden surface"></div>

      <p class="weight">250gm</p>
      <p class="roast-date">Roasted on: __ / __ / ____</p>
      <p class="best-before">Best used within 3 Months</p>
    </section>
  </main>
</body>
</html>
```